Business Cards used to invite people to our church

We are a church and have need of a business card sized advertisement that allows our members to hand them out in order to invite people to the church. I need the front of the card to say "You're Invited" or "Come Check us out". with the service times on the back of the card later.
I have attached one of the OLD cards we have used in the past, but we want a complete makeover, into a more modern style that does not require the image.
I am also replacing the old logo with a newer "flat" logo which is attached.
Please use marketing colors. (blue or red or something that catches attention)
Create a card that DOES NOT have the picture of the two people on the front
The information on the sample card back is correct to go onto new card
Target Market(s)
anyone
Industry/Entity Type
Business
Contact Information for Business Card
sertice times and address information which you can get from the sample card I uploaded. It should have "You're Invited" or "Come Check us out" on the front of the card with out logo.

```html
<!DOCTYPE html>
<html lang="en">
<head>
<meta charset="utf-8">
<title>Grace Harbor Church – Invitation Card</title>
<link href="https://fonts.googleapis.com/css2?family=Dancing+Script:wght@600&family=Jost:wght@400;700&display=swap" rel="stylesheet">
<style>
  :root {
    --backdrop: #05060c;
    --violet: #5e06a8;
    --violet-deep: #3a0470;
    --violet-glow: #a41ce8;
    --lilac: #e9a6fb;
    --white: #ffffff;
    --panel: rgba(25, 4, 45, 0.75);
  }
  * { margin: 0; padding: 0; box-sizing: border-box; }
  html, body { width: 981px; height: 1200px; overflow: hidden; }
  body { background: var(--backdrop); position: relative; font-family: "Jost", sans-serif; color: var(--white); }

  .card {
    position: absolute; left: 75px; width: 831px; height: 487px; overflow: hidden;
    background: linear-gradient(90deg, var(--violet-deep) 0%, var(--violet) 70%, #6a08b4 100%);
    box-shadow: 0 12px 30px rgba(0,0,0,0.7);
  }
  .card--front { top: 75px; }
  .card--back { top: 638px; }
  .card__curve { position: absolute; inset: 0; width: 100%; height: 100%; }

  .front__name {
    position: absolute; left: 0; right: 0; text-align: center;
    font-weight: 700; font-size: 92px; line-height: 92px; letter-spacing: 3px;
    color: var(--lilac); opacity: 0.92;
  }
  .front__name--top { top: 100px; }
  .front__name--bottom { top: 296px; }
  .band {
    position: absolute; left: 0; width: 100%;
    background: linear-gradient(90deg, rgba(255,255,255,0.95) 0%, rgba(255,255,255,0.25) 18%, rgba(255,255,255,0.12) 50%, rgba(255,255,255,0.3) 82%, rgba(255,255,255,0.95) 100%);
  }
  .band--front { top: 197px; height: 93px; }
  .front__tagline {
    position: absolute; left: 0; right: 0; top: 199px; text-align: center;
    font-family: "Dancing Script", cursive; font-weight: 600; font-size: 72px; line-height: 88px;
  }

  .back__panel {
    position: absolute; left: 51px; top: 51px; width: 724px; height: 387px;
    border-radius: 18px; background: var(--panel);
  }
  .back__contact {
    position: absolute; left: 0; right: 0; top: 78px; text-align: center;
    font-style: normal; font-size: 30px; line-height: 40px; letter-spacing: 0.5px;
  }
  .band--back { top: 235px; height: 18px; }
  .back__times {
    position: absolute; left: 85px; top: 328px; width: 440px;
    font-size: 21px; line-height: 27px; list-style: none;
  }
  .back__times li { display: flex; align-items: baseline; }
  .back__times .leader { flex: 1; border-bottom: 2px dotted var(--white); margin: 0 2px 5px; }
  .back__brand {
    position: absolute; right: 85px; top: 334px; text-align: right;
    font-weight: 700; font-size: 30px; line-height: 34px;
  }
</style>
</head>
<body>
  <section class="card card--front" aria-label="Card front">
    <svg class="card__curve" viewBox="0 0 831 487" aria-hidden="true">
      <defs>
        <radialGradient id="front-glow" cx="222" cy="150" r="300" gradientUnits="userSpaceOnUse">
          <stop offset="0" stop-color="#a41ce8"/>
          <stop offset="1" stop-color="#a41ce8" stop-opacity="0"/>
        </radialGradient>
      </defs>
      <path d="M0 0 H551 C585 190 500 390 302 487 H0 Z" fill="rgba(20,0,45,0.45)"/>
      <path d="M0 0 H551 C585 190 500 390 302 487 H0 Z" fill="url(#front-glow)"/>
    </svg>
    <div class="front__name front__name--top">GRACE</div>
    <div class="front__name front__name--bottom">HARBOR</div>
    <div class="band band--front"></div>
    <h1 class="front__tagline">Come Check us out</h1>
  </section>

  <section class="card card--back" aria-label="Card back">
    <svg class="card__curve" viewBox="0 0 831 487" aria-hidden="true">
      <path d="M0 0 H551 C585 190 500 390 302 487 H0 Z" fill="rgba(20,0,45,0.35)"/>
    </svg>
    <div class="back__panel"></div>
    <address class="back__contact">
      GRACEHARBORCHURCH.ORG<br>
      2240 N. CEDAR LANE-MAPLEWOOD, TX 75000<br>
      1-800-555-0142
    </address>
    <div class="band band--back"></div>
    <ul class="back__times">
      <li><span>SUNDAY</span><span class="leader"></span><span>9:00 AM</span></li>
      <li><span>SUNDAY</span><span class="leader"></span><span>11:00 AM</span></li>
      <li><span>Wed. Bible Class</span><span class="leader"></span><span>7:00 PM</span></li>
    </ul>
    <div class="back__brand">GRACE<br>HARBOR</div>
  </section>
</body>
</html>
```